Startup company business card (Media & Advertising)

we need a business card design for a company that is a startup in the media and aggregation industry. Card needs to look funky and of a new breed/modern and upmarket.

Target Market(s)

advertisers/ brand agencies & media publishers

Industry/Entity Type

Advertising

Contact Information for Business Card

Please ensure the front face signifies our brand (plintovo.com) and back has details for the contact. Standard contact such as phone , address, email , website etc.

Font styles to use
Other font styles liked:
• use styleguide and logo font and color

Colors

Designer to choose colors to be used in the design.

Requirements
Must have
• We are disrupting the media and agency industry so subtlety would be good to use imagery to signify this
Nice to have
• Please use logo colors for branding
Should not have
• be as creative and provide few options. Pick a brand color from logo and styleguide

```html
<!DOCTYPE html>
<html lang="en">
<head>
<meta charset="utf-8">
<title>plintovo business card</title>
<link href="https://fonts.googleapis.com/css2?family=Roboto+Slab:wght@700&family=Roboto:wght@400;500&display=swap" rel="stylesheet">
<style>
  :root {
    --bg: #8d8c8a;
    --card: #ffffff;
    --brand-red: #e83a43;
    --brand-red-dark: #c92f38;
    --brand-deep: #b21f3c;
    --ink: #111111;
    --text: #3a3a3a;
    --edge: #cfe6f4;
  }
  * { margin: 0; padding: 0; box-sizing: border-box; }
  html, body { width: 1200px; height: 913px; overflow: hidden; }
  body {
    background: var(--bg);
    font-family: "Roboto", Arial, sans-serif;
    position: relative;
  }
  .card {
    position: absolute;
    width: 600px;
    height: 350px;
    background: var(--card);
    border-radius: 18px;
    overflow: hidden;
  }
  .card--front {
    left: 70px; top: 60px;
    box-shadow: 0 6px 0 var(--brand-red), 0 9px 0 var(--brand-red-dark), 0 16px 24px rgba(0,0,0,.35);
  }
  .card--back {
    left: 540px; top: 480px;
    box-shadow: 0 6px 0 var(--edge), 0 14px 24px rgba(0,0,0,.35);
  }

  .brand {
    position: absolute;
    display: flex;
    align-items: center;
    gap: 16px;
  }
  .brand__dot {
    border-radius: 50%;
    background: var(--brand-red);
    flex: none;
  }
  .brand__name {
    font-family: "Roboto Slab", Georgia, serif;
    font-weight: 700;
    color: var(--ink);
    line-height: 1;
  }

  .card--front .brand { left: 80px; top: 120px; }
  .card--front .brand__dot { width: 64px; height: 64px; }
  .card--front .brand__name { font-size: 76px; }
  .front__url {
    position: absolute;
    left: 162px;
    top: 218px;
    font-size: 15px;
    font-weight: 500;
    letter-spacing: 9px;
    color: var(--ink);
  }

  .card--back .brand { right: 40px; top: 200px; }
  .card--back .brand__dot { width: 52px; height: 52px; }
  .card--back .brand__name { font-size: 58px; }

  .contact {
    position: absolute;
    left: 40px;
    top: 118px;
    width: 240px;
    color: var(--text);
  }
  .contact__name { color: var(--brand-deep); font-size: 22px; letter-spacing: .5px; line-height: 1.2; }
  .contact__role { font-size: 14px; margin-bottom: 12px; }
  .contact__address { font-size: 14px; line-height: 1.35; margin-bottom: 10px; padding-left: 10px; }
  .contact__list { list-style: none; font-size: 14px; padding-left: 10px; }
  .contact__list li { display: flex; align-items: center; gap: 8px; line-height: 1.5; }
  .contact__list svg { width: 13px; height: 13px; fill: var(--brand-deep); flex: none; }
</style>
</head>
<body>
  <section class="card card--front" aria-label="Card front">
    <div class="brand">
      <span class="brand__dot"></span>
      <span class="brand__name">plintovo</span>
    </div>
    <p class="front__url">www.plintovo.com</p>
  </section>

  <section class="card card--back" aria-label="Card back">
    <div class="brand">
      <span class="brand__dot"></span>
      <span class="brand__name">plintovo</span>
    </div>
    <div class="contact">
      <p class="contact__name">DANIEL VARGA</p>
      <p class="contact__role">Director</p>
      <p class="contact__address">48 Corvel Street<br>204 Lenora, Spain</p>
      <ul class="contact__list">
        <li><svg viewBox="0 0 24 24"><path d="M6.6 10.8a15 15 0 0 0 6.6 6.6l2.2-2.2a1 1 0 0 1 1-.25 11.4 11.4 0 0 0 3.6.57 1 1 0 0 1 1 1V20a1 1 0 0 1-1 1A17 17 0 0 1 3 4a1 1 0 0 1 1-1h3.5a1 1 0 0 1 1 1c0 1.25.2 2.45.57 3.57a1 1 0 0 1-.25 1z"/></svg>1234567890</li>
        <li><svg viewBox="0 0 24 24"><path d="M7 1h10a2 2 0 0 1 2 2v18a2 2 0 0 1-2 2H7a2 2 0 0 1-2-2V3a2 2 0 0 1 2-2zm0 3v14h10V4zm5 15.5a1 1 0 1 0 0 2 1 1 0 0 0 0-2z"/></svg>1234567890</li>
        <li><svg viewBox="0 0 24 24"><path d="M2 5h20v14H2zm2 2v.5l8 5 8-5V7zm0 2.8V17h16V9.8l-8 5z"/></svg>info@plintovo.com</li>
        <li><svg viewBox="0 0 24 24"><path d="M12 2a10 10 0 1 0 0 20 10 10 0 0 0 0-20zm6.9 6h-3a15 15 0 0 0-1.4-3.8A8 8 0 0 1 18.9 8zM12 4c.8 1.2 1.5 2.5 1.9 4h-3.8c.4-1.5 1.1-2.8 1.9-4zM4.3 14a8 8 0 0 1 0-4h3.4a16 16 0 0 0 0 4zm.8 2h3a15 15 0 0 0 1.4 3.8A8 8 0 0 1 5.1 16zm3-8h-3a8 8 0 0 1 4.4-3.8A15 15 0 0 0 8.1 8zM12 20c-.8-1.2-1.5-2.5-1.9-4h3.8c-.4 1.5-1.1 2.8-1.9 4zm2.3-6H9.7a14 14 0 0 1 0-4h4.6a14 14 0 0 1 0 4zm.2 5.8a15 15 0 0 0 1.4-3.8h3a8 8 0 0 1-4.4 3.8zm1.8-5.8a16 16 0 0 0 0-4h3.4a8 8 0 0 1 0 4z"/></svg>www.plintovo.com</li>
      </ul>
    </div>
  </section>
</body>
</html>
```